Simple landing page for Brindleys cookbook

I need a one page landingpage where customers can order the cookbook.
This is a cookbook of a collection of recipes from our deli that we used to run.
I need a landing page where customers can come and order the book. I also need it coded. I already have the domain through hostmoxa.
I can send the file of the book through wetransfer. It's too big to upload here. Just so you get the feel that I am looking for.
I attached a simple text as an introduction to the page. But I am open to any suggestions. I want it all to be about the experience that we are sharing the recipes with everybody and that it's for sale. The book is $29.99, shipping included.
Customers have to be able to click and buy the book from it.

Coding

Coded - Design and coding required

Number of Pages Required

1 page

Font styles to use
Sans Serif

Requirements
Must have
• Same colors as the cookbook

```html
<!DOCTYPE html>
<html lang="en">
<head>
<meta charset="utf-8">
<title>Brindleys Cookbook</title>
<link href="https://fonts.googleapis.com/css2?family=Great+Vibes&family=Lato:ital,wght@0,300;0,400;0,700;0,900;1,400&display=swap" rel="stylesheet">
<style>
  :root {
    --navy-deep: #020d1e;
    --navy: #041328;
    --hero-blue: #1b2c4d;
    --hero-blue-dark: #0c1730;
    --orange: #ec6a25;
    --white: #ffffff;
    --black: #000000;
    --footer-text: #f2f2f2;
  }
  * { margin: 0; padding: 0; box-sizing: border-box; }
  html, body { width: 1125px; height: 1200px; overflow: hidden; }
  body {
    position: relative;
    background: var(--navy);
    color: var(--white);
    font-family: "Lato", sans-serif;
  }
  .sidebar {
    position: absolute; left: 0; top: 0;
    width: 272px; height: 513px;
    background: var(--navy-deep);
  }
  .brand {
    position: absolute; left: 47px; top: 40px;
    font-family: "Lato", sans-serif;
    font-weight: 300;
    font-size: 36px;
    line-height: 48px;
    color: var(--white);
  }
  .nav { list-style: none; }
  .nav-item {
    position: absolute; left: 95px;
    font-size: 15px; letter-spacing: 0.2px;
    color: var(--white);
    text-decoration: none;
  }
  .nav-item.is-active::after {
    content: ""; position: absolute; left: -3px; top: 26px;
    width: 57px; height: 2px; background: var(--orange);
  }
  .hero-photo {
    position: absolute; left: 272px; top: 0;
    width: 853px; height: 513px;
    background: radial-gradient(ellipse at 63% 55%, #3a3a2e 0%, #1a2130 38%, var(--hero-blue) 60%, var(--hero-blue-dark) 100%);
  }
  .intro {
    position: absolute; left: 134px; top: 560px; width: 493px;
  }
  .intro-title {
    font-family: "Great Vibes", cursive;
    font-weight: 400;
    font-size: 52px;
    line-height: 60px;
    margin-bottom: 30px;
  }
  .intro-text p {
    font-style: italic;
    font-size: 13.5px;
    line-height: 16.5px;
    letter-spacing: -0.2px;
    margin-bottom: 16.5px;
  }
  .buy-button {
    position: absolute; left: 134px; top: 1000px;
    width: 162px; height: 58px;
    border-radius: 29px;
    background: var(--orange);
    color: var(--white);
    font-weight: 900; font-size: 18px; letter-spacing: -0.4px;
    display: flex; align-items: center; justify-content: center;
    text-decoration: none;
  }
  .book-cover {
    position: absolute; left: 718px; top: 581px;
    width: 349px; height: 467px;
    background: linear-gradient(160deg, #f4f6f8 0%, #e6e9ec 55%, #c99a55 75%, #e9ecef 100%);
    border-left: 10px solid #3a3a3a;
    border-bottom: 4px solid #9a9a9a;
  }
  .price-badge {
    position: absolute; left: 676px; top: 586px;
    width: 91px; height: 91px; border-radius: 50%;
    background: var(--black);
    border: 3px solid var(--white);
    text-align: center;
  }
  .price-amount {
    display: block; margin-top: 22px;
    color: var(--orange); font-weight: 700; font-size: 22.5px; line-height: 24px;
  }
  .price-note { display: block; font-size: 8px; margin-top: 3px; }
  .site-footer {
    position: absolute; left: 0; top: 1113px;
    width: 1125px; height: 87px;
    background: var(--black);
    color: var(--footer-text);
    font-size: 13.5px;
    text-align: center;
    line-height: 87px;
  }
  .site-footer a { color: var(--footer-text); text-decoration: none; }
</style>
</head>
<body>
  <aside class="sidebar">
    <div class="brand">Brindleys<br>Cookbook</div>
    <nav>
      <ul class="nav">
        <li><a class="nav-item is-active" href="#" style="top:221px">HOME</a></li>
        <li><a class="nav-item" href="#" style="top:271px">ABOUT</a></li>
        <li><a class="nav-item" href="#" style="top:320px">RECIPES</a></li>
        <li><a class="nav-item" href="#" style="top:370px">BOOKS</a></li>
        <li><a class="nav-item" href="#" style="top:419px">CONTACT</a></li>
      </ul>
    </nav>
  </aside>

  <div class="hero-photo" role="img" aria-label="Top-down photo of a plate of grilled meat, salad and fries on a dark blue table with sauce, greens and cutlery"></div>

  <section class="intro">
    <h1 class="intro-title">Introduction</h1>
    <div class="intro-text">
      <p>Opening it's doors in January of 2010, Brindleys European Deli was a sandwich shop in Harrowfield, New Avalon, but also a lot more than that.</p>
      <p>We spent five years with this business until it's eventual closure in April of 2015. It was a special time where we met tons of amazing people, who we loved to see and serve.</p>
      <p>Brindleys started out as a deli but eventually morphed into the sandwich shop we all know it as today.</p>
      <p>We are overwhelmed with the continuous positive messages and comments we get on our Chatterly page that is still up and running.</p>
      <p>Unfortunately, we can't open another Brindleys, but we can offer you this collection of our recipes for you to try out at home with your family and friends.</p>
      <p>We truly hope you will enjoy making these sandwiches just as much as we did.</p>
      <p>If you do, please post your pictures of you making a meal or the finished product, or even enjoying it!</p>
    </div>
  </section>

  <a class="buy-button" href="#">BUY IT NOW</a>

  <div class="book-cover" role="img" aria-label="Cookbook cover showing a sandwich with cured meat and greens, titled Brindleys Sandwiches, 28 recipes"></div>

  <div class="price-badge">
    <span class="price-amount">$29.99</span>
    <span class="price-note">Shipping included</span>
  </div>

  <footer class="site-footer">
    © 2022 Brindleys Cookbook. All rights reserved &nbsp;|&nbsp; <a href="#">Privacy</a> &nbsp;| <a href="#">Terms of Use</a>
  </footer>
</body>
</html>
```